Heronby Mortgage Capital Business Card

We need a business card design for our mortgage servicing company. In addition to servicing the loans of homeowners, we help homeowners with purchasing their homes and any mortgage refinancing. We would like to see designs that use the colors in the logo attached below (gold-ish yellow and navy blue), and any other design you deem fit! The design should communicate a simpler life with smart mortgages provided by Heronby.

```html
<!DOCTYPE html>
<html lang="en">
<head>
<meta charset="utf-8">
<title>Heronby Mortgage Capital – Business Card</title>
<link href="https://fonts.googleapis.com/css2?family=Abhaya+Libre:wght@400;700&display=swap" rel="stylesheet">
<style>
  :root {
    --stage: #b3b3b3;
    --gold: #dfb03e;
    --navy: #27215a;
    --white: #ffffff;
    --ink: #1c1c1c;
    --rule: #111111;
  }
  * { margin: 0; padding: 0; box-sizing: border-box; }
  html, body {
    width: 1154px; height: 1200px; overflow: hidden;
    background: var(--stage);
    font-family: "Abhaya Libre", Georgia, serif;
  }
  .canvas { position: relative; width: 1154px; height: 1200px; }

  .card {
    position: absolute;
    border-radius: 28px;
    box-shadow: 0 8px 10px rgba(0,0,0,0.12);
    overflow: hidden;
  }
  .card--front { left: 191px; top: 138px; width: 770px; height: 440px; background: var(--gold); }
  .card--back  { left: 191px; top: 620px; width: 773px; height: 442px; background: var(--white); }

  .brand {
    position: absolute;
    color: var(--navy);
    font-weight: 700;
    line-height: 1;
    text-align: center;
  }
  .brand__name { display: block; letter-spacing: 0.5px; }
  .brand__sub  { display: block; letter-spacing: 2px; margin-top: 4px; }

  .card--front .brand { left: 0; right: 0; top: 170px; }
  .card--front .brand__name { font-size: 84px; }
  .card--front .brand__sub  { font-size: 24px; }

  .card--back .brand { left: 390px; width: 330px; top: 58px; }
  .card--back .brand__name { font-size: 62px; }
  .card--back .brand__sub  { font-size: 18px; }

  .holder { position: absolute; left: 46px; top: 250px; }
  .holder__name {
    font-size: 29px; font-weight: 700; color: var(--navy);
    letter-spacing: 0.6px; line-height: 1;
  }
  .holder__role {
    margin-top: 10px;
    font-size: 18px; font-weight: 400; color: var(--ink);
    letter-spacing: 0.6px; line-height: 1;
  }

  .divider {
    position: absolute; left: 46px; right: 47px; top: 323px;
    height: 2px; background: var(--rule);
  }

  .contacts { position: absolute; left: 46px; top: 338px; list-style: none; }
  .contacts__item {
    display: flex; align-items: center; gap: 12px;
    height: 30.5px;
    font-size: 19px; color: var(--ink);
  }
  .contacts__icon { width: 19px; height: 19px; flex: none; }

  .address {
    position: absolute; right: 47px; top: 358px;
    text-align: right; font-size: 19px; line-height: 26px; color: var(--ink);
    font-style: normal;
  }
</style>
</head>
<body>
<main class="canvas">

  <section class="card card--front" aria-label="Card front">
    <div class="brand">
      <span class="brand__name">Heronby</span>
      <span class="brand__sub">MORTGAGE</span>
    </div>
  </section>

  <section class="card card--back" aria-label="Card back">
    <div class="brand">
      <span class="brand__name">Heronby</span>
      <span class="brand__sub">MORTGAGE</span>
    </div>

    <div class="holder">
      <h1 class="holder__name">OWEN CASTELL</h1>
      <p class="holder__role">MANAGING DIRECTOR</p>
    </div>

    <div class="divider"></div>

    <ul class="contacts">
      <li class="contacts__item">
        <svg class="contacts__icon" viewBox="0 0 24 24" aria-hidden="true">
          <path fill="var(--gold)" d="M6.6 10.8a15.1 15.1 0 0 0 6.6 6.6l2.2-2.2c.3-.3.7-.4 1-.2 1.1.4 2.3.6 3.6.6.6 0 1 .4 1 1V20c0 .6-.4 1-1 1C10.6 21 3 13.4 3 4c0-.6.4-1 1-1h3.5c.6 0 1 .4 1 1 0 1.3.2 2.5.6 3.6.1.3 0 .7-.2 1L6.6 10.8z"/>
          <path fill="none" stroke="var(--gold)" stroke-width="1.6" d="M14 3.5a7 7 0 0 1 6.5 6.5M14 7a3.5 3.5 0 0 1 3 3"/>
        </svg>
        <span>044-987 654 321</span>
      </li>
      <li class="contacts__item">
        <svg class="contacts__icon" viewBox="0 0 24 24" aria-hidden="true">
          <rect x="2" y="5" width="20" height="14" fill="var(--gold)"/>
          <path fill="none" stroke="var(--white)" stroke-width="1.5" d="M2 5l10 8 10-8M2 19l7-6M22 19l-7-6"/>
        </svg>
        <span>info@heronbymail.com</span>
      </li>
      <li class="contacts__item">
        <svg class="contacts__icon" viewBox="0 0 24 24" aria-hidden="true">
          <g fill="none" stroke="var(--gold)" stroke-width="2">
            <circle cx="12" cy="12" r="10"/>
            <ellipse cx="12" cy="12" rx="4.5" ry="10"/>
            <path d="M2 12h20M4 7h16M4 17h16"/>
          </g>
        </svg>
        <span>www.heronbycapital.com</span>
      </li>
    </ul>

    <address class="address">
      418, Harbour View Road<br>
      45210, Westmark
    </address>
  </section>

</main>
</body>
</html>
```